Plant Based Planner Graphics - Animals, Doctor Portraits & Charts

I am looking for a few custom graphics to use in a Plant Based Daily Planner. I would love some fun renditions of some famous plant based doctors to use on the pages featuring them. Then also a few plant inspired graphics that I can use throughout the planner. This is for print for sale.
Hoping to work with one designer on the entire project but please feel free to provide any one of the following graphics for me to consider you for the whole project.
~Doctors Likeness Graphics of:Dr. T.C. CampbellDr. EsselysteinDr. GregerDr. Owen Lustig
~Macro Ratio Pie Chart for Whole Food Plant Based showing 75-80% Carbs, 10-15% Fat and 10-15% Protein
~One graphic of someone sleeping dreaming about vegetables
~Cute graphic of a happy Fish, Honey Bee, Chicken and Cow - all separate graphics
~One Graphic of Kale, Spinach, Lettuce and Beet Greens - one graphic
~One Graphic of what Inflammation is associated with: Cardiovascular Disease, Diabetes, Arthritis, Autoimmune Disease, Lung Diseases, Neurological Diseases, Alzheimer Disease
~ One Simple Graphic Asking "Does it make sense to use 9 Plant Based Calories to make 1 Animal Based Calorie?"Would like to avoid harsh primary colors.
I included a suggest color palette. I am also using the font "quicksand" if that is an option. Attached Files are only inspiration.
Updates
Target Market(s)
20-15 Year Old Health and Environmental Conscious Readers
Font styles to use
Other font styles liked:
- Quicksand
Requirements
Should not have
- No depictions of Animal Food Products, Oil, or Processed Foods.

```html
<!DOCTYPE html>
<html lang="en">
<head>
<meta charset="utf-8">
<title>Macro Ratio Pie Chart for Whole Food Plant Based Macros</title>
<link rel="stylesheet" href="https://fonts.googleapis.com/css2?family=Montserrat:wght@600;700;800&display=swap">
<style>
  :root {
    --page: #e6e6e6;
    --panel-light: #f1f1f1;
    --panel-dark: #dedede;
    --lime: #a8cf38;
    --teal: #33b8a6;
    --purple: #6a449b;
    --ink: #272727;
    --white: #ffffff;
    --ring-grey: #cfcfcf;
    --ring-lilac: #ddd4ea;
  }
  html, body {
    margin: 0;
    width: 1138px;
    height: 1200px;
    overflow: hidden;
    background: var(--page);
  }
  .macro-chart {
    display: block;
    width: 1138px;
    height: 1200px;
    font-family: "Montserrat", sans-serif;
  }
  .header-title {
    fill: var(--white);
    font-weight: 700;
    font-size: 43px;
  }
  .arc-label {
    fill: var(--white);
    font-weight: 700;
    font-size: 58px;
    letter-spacing: 4px;
  }
  .center-label {
    fill: var(--ink);
    font-weight: 800;
    font-size: 54px;
  }
  .slice-label {
    fill: var(--white);
    font-weight: 700;
    font-size: 35px;
  }
</style>
</head>
<body>
<svg class="macro-chart" viewBox="0 0 1180 1295" preserveAspectRatio="xMidYMid meet" role="img" aria-label="Macro ratio pie chart for whole food plant based eating: 75-80% good carbs, 10-15% fat, 10-15% protein">
  <defs>
    <radialGradient id="panelShade" cx="50%" cy="45%" r="70%">
      <stop offset="0" stop-color="var(--panel-light)"/>
      <stop offset="1" stop-color="var(--panel-dark)"/>
    </radialGradient>
    <path id="carbArc" d="M312 632 A290 290 0 0 1 872 632"/>
  </defs>

  <!-- panel -->
  <rect class="panel" width="1180" height="1295" fill="url(#panelShade)"/>

  <!-- header band -->
  <rect class="header-band" width="1180" height="113" fill="var(--lime)"/>
  <text class="header-title" x="590" y="82" text-anchor="middle">Macro Ratio Pie Chart for Whole WFPB MACROS</text>

  <!-- outer ring -->
  <g class="outer-ring" fill="none" stroke-width="13">
    <path d="M127 806 A475 475 0 1 1 1057 806" stroke="var(--purple)"/>
    <path d="M551 1180 A475 475 0 0 1 155 893" stroke="var(--teal)"/>
    <path d="M1029 893 A475 475 0 0 1 633 1180" stroke="var(--lime)"/>
  </g>

  <!-- pie slices -->
  <g class="pie">
    <circle cx="592" cy="707" r="435" fill="var(--purple)"/>
    <path class="slice-fat" d="M592 707 L592 1142 A435 435 0 0 1 176 834 Z" fill="var(--teal)"/>
    <path class="slice-protein" d="M592 707 L1008 834 A435 435 0 0 1 592 1142 Z" fill="var(--lime)"/>
    <circle class="inner-shade" cx="592" cy="707" r="198" fill="#000" opacity="0.13"/>
    <g class="slice-gaps" stroke="var(--white)" stroke-width="26">
      <line x1="592" y1="707" x2="140" y2="845"/>
      <line x1="592" y1="707" x2="1044" y2="845"/>
      <line x1="592" y1="707" x2="592" y2="1190"/>
    </g>
  </g>

  <!-- center hub -->
  <circle cx="592" cy="707" r="158" fill="var(--white)"/>
  <circle cx="592" cy="707" r="145" fill="none" stroke="var(--ring-lilac)" stroke-width="7"/>
  <text class="center-label" x="592" y="700" text-anchor="middle">FOOD</text>
  <text class="center-label" x="592" y="756" text-anchor="middle">PLANT</text>

  <!-- labels -->
  <text class="arc-label"><textPath href="#carbArc" startOffset="50%" text-anchor="middle">75-80% GOOD CARBS</textPath></text>
  <text class="slice-label" x="422" y="915" text-anchor="middle">10-15%</text>
  <text class="slice-label" x="417" y="960" text-anchor="middle">FAT</text>
  <text class="slice-label" x="752" y="915" text-anchor="middle">10-15%</text>
  <text class="slice-label" x="748" y="960" text-anchor="middle">PROTEIN</text>

  <!-- icon badges -->
  <g class="badge badge-carbs">
    <circle cx="592" cy="257" r="112" fill="var(--ring-grey)"/>
    <circle cx="592" cy="257" r="102" fill="var(--white)"/>
    <circle cx="592" cy="257" r="92" fill="none" stroke="var(--ring-lilac)" stroke-width="5"/>
    <circle cx="592" cy="257" r="60" fill="#e7def2" role="img" aria-label="Corn, apple and wheat illustration in purple"/>
  </g>
  <g class="badge badge-fat">
    <circle cx="317" cy="1082" r="112" fill="var(--ring-grey)"/>
    <circle cx="317" cy="1082" r="102" fill="var(--white)"/>
    <circle cx="317" cy="1082" r="92" fill="none" stroke="var(--ring-lilac)" stroke-width="5"/>
    <path class="drop-icon" d="M317 1020 C300 1050 276 1075 276 1102 A41 41 0 0 0 358 1102 C358 1075 334 1050 317 1020 Z" fill="var(--teal)"/>
    <path d="M302 1075 C292 1092 290 1110 300 1125" fill="none" stroke="var(--white)" stroke-width="6" stroke-linecap="round"/>
  </g>
  <g class="badge badge-protein">
    <circle cx="865" cy="1082" r="112" fill="var(--ring-grey)"/>
    <circle cx="865" cy="1082" r="102" fill="var(--white)"/>
    <circle cx="865" cy="1082" r="92" fill="none" stroke="var(--ring-lilac)" stroke-width="5"/>
    <circle cx="865" cy="1082" r="60" fill="#e4f0c4" role="img" aria-label="Beans, nuts and grain illustration in green"/>
  </g>

  <!-- footer rule -->
  <rect class="footer-rule" y="1281" width="1180" height="14" fill="var(--teal)"/>
</svg>
</body>
</html>
```